NorthPlain Bytes Yellow rose letterhead

I have a new logo for my company but in its current form it is too large to be used on letterhead or as a email signature. I need to have the designer use elements from the current logo and create something close to the original but more suited for smaller items.
Updates

I just uploaded a copy of our logo that does not have the weathered affect. Thanks

Industry/Entity Type

It Company

Requirements
Must have
• The design must maintain the visual effect of the current logo. It needs to include the yellow rose and the name of the company.
Nice to have
• It would be nice to maintain the stamp theme and incorporate my name, address, phone, email. etc.

```html
<!DOCTYPE html>
<html lang="en">
<head>
<meta charset="utf-8">
<title>NorthPlain Bytes Letterhead</title>
<link rel="stylesheet" href="https://fonts.googleapis.com/css2?family=Open+Sans:wght@400;600;700&display=swap">
<style>
  :root {
    --backdrop: #8a8a8a;
    --paper: #f4f4f2;
    --ink: #2a2a2a;
    --teal: #3fb8c2;
    --teal-deep: #2aa7a9;
    --logo-brown: #4a3a33;
    --rose-yellow: #f2c62a;
    --rose-light: #fbe27a;
    --rose-deep: #e9a91c;
    --signature-blue: #2c3f8f;
  }
  * { box-sizing: border-box; margin: 0; padding: 0; }
  html, body {
    width: 1200px; height: 900px; overflow: hidden;
    background: var(--backdrop);
    font-family: "Open Sans", Arial, sans-serif;
    color: var(--ink);
  }
  .letterhead {
    position: absolute; left: 290px; top: 12px;
    width: 620px; height: 876px;
    background: var(--paper);
    box-shadow: 0 6px 24px rgba(0,0,0,0.25);
    overflow: hidden;
  }
  .tagline {
    position: absolute; top: 70px; right: 48px;
    text-align: right; color: var(--teal);
    font-size: 9px; line-height: 1.3; font-weight: 600;
  }
  .tagline-title { font-size: 11px; font-weight: 700; letter-spacing: 0.6px; }
  .brand {
    position: absolute; top: 196px; left: 48px;
    display: flex; align-items: center; gap: 8px;
  }
  .brand-square { width: 22px; height: 22px; background: var(--rose-yellow); }
  .brand-name { font-size: 17px; font-weight: 700; color: var(--logo-brown); }
  .recipient {
    position: absolute; top: 262px; left: 150px;
    font-size: 9.5px; line-height: 1.45; font-style: normal;
  }
  .letter-body {
    position: absolute; top: 330px; left: 150px; width: 420px;
    font-size: 9.5px; line-height: 1.5;
  }
  .letter-body p { margin-bottom: 14px; text-align: justify; }
  .letter-body .salutation { margin-bottom: 10px; }
  .signature-mark {
    width: 140px; height: 30px; margin-top: 4px;
    background: linear-gradient(90deg, rgba(44,63,143,0.15), rgba(44,63,143,0.05));
  }
  .sign-off { font-size: 9.5px; line-height: 1.45; margin-top: 6px; }
  .footer-line {
    position: absolute; left: 60px; bottom: 86px;
    font-size: 7.5px; font-weight: 600; color: var(--teal);
    white-space: nowrap;
  }
  .footer-band { position: absolute; left: 0; bottom: 0; width: 620px; height: 78px; }
  .band-corner { position: absolute; left: 0; bottom: 0; }
  .band-art {
    position: absolute; left: 48px; bottom: 0; width: 572px; height: 78px;
    background: radial-gradient(ellipse at 60% 40%, var(--rose-light), var(--rose-yellow) 55%, var(--rose-deep));
  }
</style>
</head>
<body>
  <main class="letterhead">
    <header>
      <div class="tagline">
        <div class="tagline-title">THE INSIGHT BUILDERS</div>
        <div>Shaping Clearer Answers</div>
        <div>From Everyday Information</div>
      </div>
      <div class="brand">
        <span class="brand-square"></span>
        <span class="brand-name">NorthPlain Bytes</span>
      </div>
    </header>

    <address class="recipient">
      Marion Hale<br>214 Linden Ave<br>Easton MA
    </address>

    <section class="letter-body">
      <p class="salutation">Dear Mrs Marion Hale,</p>
      <p>Lorem ipsum dolor sit amet, consectetur adipiscing elit. Integer aliquet diam eget mi rutrum consectetur et id orci. Praesent vitae felis vitae justo elementum tincidunt. Duis pharetra turpis semper dui elementum nec aliquet lectus pulvinar. Donec condimentum mattis diam, id congue risus congue a. Maecenas commodo, nisi a gravida condimentum, elit erat condimentum leo, in pellentesque elit erat id nisl. Pellentesque consequat faucibus dictum. Nam tincidunt viverra elit at hendrerit. Quisque eget purus tellus. Mauris mattis nunc nec nisi pulvinar consectetur.</p>
      <p>Nunc molestie iaculis orci, vitae consequat mi condimentum vitae. Etiam et tortor velit. Sed ac magna tellus. Proin quam augue, vehicula sed euismod in, vehicula eu felis. Pellentesque a orci ac turpis commodo varius at ut arcu. Integer viverra semper sapien fermentum egestas. Curabitur erat purus, congue et faucibus sit amet, fringilla elementum odio. Sed pretium tincidunt mi, nec fermentum urna interdum sed. Nam et lectus turpis, quis cursus ipsum. Maecenas non nibh odio. Sed in laoreet justo.</p>
      <p>Aenean sed sem lacus. Vivamus auctor, sapien nec aliquet ultrices, mauris turpis porttitor nisi, id rutrum velit erat non urna. Praesent eu augue eu ligula feugiat malesuada. Proin nec nibh erat. Sed et leo id leo volutpat viverra non ac mi. In quis dictum magna. Donec at dui sed dui tristique dictum. Donec varius sapien sed turpis dictum a dignissim diam facilisis.</p>
      <div class="signature-mark" role="img" aria-label="Handwritten signature of Vera Lindqvist in blue ink"></div>
      <div class="sign-off">Yours Sincerely<br>Vera Lindqvist</div>
    </section>

    <footer>
      <div class="footer-line">Vera Lindqvist, PhD &bull; 88 Prairie Loop, Ste 400, Fargo ND 58102 &bull; vera@northplainbytes.com &bull; 1-800-555-0147</div>
      <div class="footer-band">
        <svg class="band-corner" width="48" height="78" viewBox="0 0 48 78">
          <polygon points="0,0 48,78 0,78" fill="var(--teal-deep)"/>
        </svg>
        <div class="band-art" role="img" aria-label="Close-up illustration of a yellow rose with dew drops"></div>
      </div>
    </footer>
  </main>
</body>
</html>
```